Horseriders ecommerce

I need the design of a web site and ecommerce for horse riders product. the actual site is brenvatoro.it and is completely to rebuild.
the most important thing that must come out from the design is that this shop sells products for both type of riding: english and western and as well has products available and good for both. (accessories and horse care)
the site owners loves much more the western riding and they want to gain a good part of customers of it, that's why i ask you to give the central area and importance to the western products.
at http://www.plokimart.com you can see a site style that we like, especially for the inner pages of products.
colors and graphics elements must be related to the world of horse riding, but we want the design to keep elegance and style, without being so western!
you need to find a way to create a cool design, user friendly to buy and that gives the real impression of professionality and care.
please check this site: http://www.quintelbazar.it/
the style is not so nice in my opinion, but somehow the navigation is friendly
in attachment to the project I add the mockup of the home page. Abou the inner page, please feel free to create the correct layout and check the one of www.plokimart.com which I like especially for the product sheet.

p.s. you can change the color of the logo
Updates

Hello dear designers,
i've pushed a little the deadline.
I will give you feedback in a while.
thaks to all
Gisetta

Target Market(s)

horse riders
western riders
english riders
stables owners

Industry/Entity Type

Product

Requirements
Must have
• style, elegance and western atmosphere. GOOD SPACES to show products.
• MUST HAVE a base way to manage banners in home page
Nice to have
• images of horses, but the most important images are products
Should not have
• too many western elements

```html
<!DOCTYPE html>
<html lang="en">
<head>
<meta charset="utf-8">
<title>Brenvatoro – Horse Equipment Specialists</title>
<link rel="stylesheet" href="https://fonts.googleapis.com/css2?family=Tinos:wght@400;700&family=Raleway:wght@400;700&display=swap">
<style>
:root{
  --ink:#1d1916;
  --bar:#1f1b18;
  --band:rgba(38,24,16,.84);
  --cream:#e4d4b4;
  --white:#ffffff;
  --orange:#ef8a14;
  --rust:#8e2a0c;
  --rust-line:#c2623a;
  --footer:#2b1810;
  --frame:#dccab0;
  --link:#e0600c;
  --date:#8e2a0c;
  --text:#222;
}
*{box-sizing:border-box;margin:0;padding:0}
html,body{width:822px;height:1200px;overflow:hidden}
body{position:relative;background:var(--cream);font-family:"Tinos",serif;color:var(--text)}
.abs{position:absolute}

/* top bar */
.topbar{left:0;top:0;width:822px;height:28px;background:var(--bar);font-family:"Raleway",sans-serif;font-size:7.5px;color:#fff;z-index:2}
.topbar .welcome{left:74px;top:10px}
.topbar .links{left:282px;top:10px;display:flex}
.topbar .links span{padding:0 9px;border-left:1px solid #444}
.topbar .links span:first-child{border:0}
.topbar .cart{left:513px;top:9px;display:flex;align-items:center;gap:6px}
.topbar .total{left:577px;top:10px}
.social{top:0;width:34px;height:37px;background:var(--orange);display:flex;align-items:center;justify-content:center;clip-path:polygon(0 0,100% 0,100% 100%,50% 88%,0 100%);z-index:3}
.social span{width:10px;height:10px;background:#fff;border-radius:50%;margin-top:-4px}
.social.one{left:668px}
.social.two{left:711px}

/* hero */
.hero{left:0;top:28px;width:822px;height:413px;background:
  radial-gradient(ellipse 150px 120px at 560px 110px,rgba(250,220,180,.95) 0%,rgba(230,170,110,.55) 50%,transparent 100%),
  radial-gradient(ellipse 120px 150px at 690px 250px,rgba(220,150,90,.7) 0%,transparent 100%),
  radial-gradient(ellipse 300px 140px at 700px 80px,rgba(200,120,50,.6) 0%,transparent 100%),
  linear-gradient(90deg,rgba(0,0,0,.75) 0%,rgba(0,0,0,.35) 40%,transparent 65%),
  linear-gradient(180deg,#2a1608 0%,#4a260e 40%,#6a3410 55%,#c27228 75%,#e8a040 88%,#b8701e 100%)}
.hero-copy{left:92px;top:81px;color:#fff;text-transform:uppercase}
.hero-copy .kicker{font-size:19px;letter-spacing:.2px}
.hero-copy h1{font-weight:400;font-size:31px;line-height:28px;margin-top:10px}
.hero-btn{left:92px;top:178px;width:110px;height:23px;font-size:14px;line-height:23px;background:var(--orange);color:var(--ink);text-transform:uppercase;text-align:center;letter-spacing:.4px}
.navband{left:0;top:271px;width:822px;height:59px;background:var(--band)}
.nav{left:314px;top:271px;display:flex;height:59px;font-size:8.5px;text-transform:uppercase}
.nav a{display:block;padding:0 16px;line-height:59px;color:#fff;text-decoration:none}
.nav a.current{background:rgba(20,12,8,.85);padding:0 8px;margin-right:8px}
.logo{left:97px;top:249px;width:154px;height:111px;border-radius:50%;background:radial-gradient(ellipse at 50% 40%,#c29468,#a87850);border:3px solid #fff;box-shadow:0 0 0 3px #6b4a34;display:flex;align-items:center;justify-content:center;color:#fff;font-size:19px}
.logo .mark{width:10px;height:10px;background:#fff;margin-right:6px}
.dots{left:672px;top:388px;display:flex;gap:5px}
.dots i{width:8px;height:8px;border-radius:50%;background:#fff;display:block}
.dots i:first-child{background:var(--orange);border:2px solid #fff}

/* main panel */
.panel{left:75px;top:416px;width:671px;height:725px;background:var(--white)}
.tile{top:432px;width:136px;height:230px;background:var(--frame);padding:5px}
.tile .photo{width:100%;height:100%;text-align:center;color:#fff;text-transform:uppercase;padding-top:26px;text-shadow:0 1px 2px rgba(0,0,0,.4)}
.tile .photo small{display:block;font-size:11px}
.tile .photo b{display:block;font-weight:400;font-size:19px;line-height:20px}
.tile.english{left:95px}
.tile.english .photo{background:
  radial-gradient(circle 18px at 85px 195px,#fff6e0 0%,#ffd28a 55%,transparent 100%),
  radial-gradient(ellipse 70px 40px at 85px 195px,rgba(255,160,60,.9),transparent 100%),
  radial-gradient(ellipse 55px 60px at 60px 110px,rgba(120,40,20,.85),transparent 100%),
  linear-gradient(180deg,#1c0a06 0%,#3a1008 25%,#7a1c0c 50%,#d2401a 72%,#f06a1c 85%,#4a1408 96%)}
.tile.western{left:240px}
.tile.western .photo{background:
  radial-gradient(ellipse 30px 70px at 80px 130px,rgba(200,120,90,.9),rgba(40,50,90,.7) 70%,transparent 100%),
  radial-gradient(ellipse 40px 60px at 22px 90px,rgba(90,50,30,.95),transparent 100%),
  radial-gradient(ellipse 60px 25px at 100px 45px,rgba(255,255,255,.8),transparent 100%),
  linear-gradient(180deg,#3a7fcf 0%,#8cbbe6 38%,#c8dcee 52%,#9ab870 78%,#5c9a2c 90%,#4a8a24 100%)}
.tile.care{left:385px}
.tile.care .photo{color:var(--ink);text-shadow:none;background:
  radial-gradient(ellipse 60px 35px at 75px 125px,rgba(40,22,12,.95),transparent 100%),
  radial-gradient(ellipse 35px 30px at 30px 130px,rgba(50,28,14,.9),transparent 100%),
  linear-gradient(180deg,#f6a24a 0%,#eaa658 25%,#c88040 45%,#6a4420 62%,#8a6430 80%,#a47c3c 100%)}

.promo{color:#fff;text-transform:uppercase;text-align:center}
.gift{left:95px;top:680px;width:174px;height:80px;background:var(--orange);padding-top:15px}
.gift .t1{font-size:15px;line-height:15px}
.gift .t2{font-size:9.5px;color:var(--ink)}
.gift hr{border:0;border-top:1px solid #fff;width:120px;margin:5px auto}
.gift .t3{font-size:13px}
.stables{left:274px;top:680px;width:247px;height:80px;padding-top:8px;background:
  radial-gradient(ellipse 90px 30px at 120px 20px,rgba(200,150,100,.55),transparent 100%),
  linear-gradient(90deg,rgba(20,10,4,.6),transparent 25%,transparent 75%,rgba(20,10,4,.6)),
  linear-gradient(180deg,#4a2c16,#6a4424 45%,#3a2210 75%,#1e1208)}
.stables .t1{font-size:19px;line-height:19px}
.stables .t2{font-size:9.5px}
.small-btn{display:inline-block;background:#f0b36a;color:var(--ink);font-size:8px;padding:0 16px;line-height:14px;margin-top:10px}
.ship{left:95px;top:770px;width:211px;height:62px;color:var(--ink);text-align:right;padding:6px 8px 0 0;background:
  radial-gradient(ellipse 60px 24px at 70px 42px,rgba(255,255,255,.95),rgba(220,224,230,.6) 60%,transparent 100%),
  linear-gradient(90deg,#aab2be,#dfe3e8 35%,#f4f4f4 65%,#e6e8ec)}
.ship .t1{font-size:12px;line-height:12px}
.ship .t2{font-size:7.5px}
.best{left:310px;top:770px;width:211px;height:62px;padding-top:8px;background:
  radial-gradient(ellipse 50px 28px at 50px 40px,rgba(160,110,70,.8),transparent 100%),
  linear-gradient(90deg,#2e1e12,#6a4a2e 45%,#4a3220 75%,#1e140c)}
.best .t1{font-size:17px;line-height:16px}
.best .t2{font-size:7.5px}
.best .small-btn{background:var(--orange);margin-top:4px;padding:0 18px}

.news{left:95px;top:852px;width:326px;height:198px;border:1px solid #8a5a3c;border-radius:3px;padding:8px 17px}
.news h2{font-weight:400;font-size:14px;text-transform:uppercase;padding-bottom:4px;border-bottom:1px solid #8a5a3c;width:284px;color:var(--ink)}
.news .item{margin-top:10px;font-size:8px;line-height:10px}
.news .date{color:var(--date);font-size:7.5px;margin-bottom:3px}
.news a{color:var(--link);font-weight:700;text-decoration:underline}
.news .more{display:block;margin-top:10px;font-size:8px;font-weight:700;color:var(--link);text-decoration:none}
.saddle{left:427px;top:852px;width:94px;height:198px;padding-top:70px;background:
  radial-gradient(ellipse 45px 55px at 47px 45px,rgba(150,80,40,.8),transparent 100%),
  radial-gradient(ellipse 50px 50px at 47px 170px,rgba(160,90,45,.75),transparent 100%),
  linear-gradient(180deg,#26331e,#3e3a22 30%,#5a3a22 60%,#2a1a10)}
.saddle .t1{font-size:9px}
.saddle .t2{font-size:15px;line-height:15px}
.saddle .small-btn{background:var(--orange);font-size:8.5px;padding:2px 7px;margin-top:12px}

/* sidebar */
.sidebar{left:538px;top:416px;width:208px;height:634px;background:var(--rust);color:#fff;padding:21px 26px 0}
.search{display:flex;height:16px}
.search .field{flex:1;background:#fff;color:#222;font-size:7px;line-height:16px;padding-left:8px}
.search .go{width:47px;background:var(--orange);color:var(--ink);font-size:7.5px;line-height:16px;text-align:center}
.divider{display:flex;align-items:center;margin:20px 0 6px}
.divider::before,.divider::after{content:"";flex:1;border-top:1px solid var(--orange)}
.divider i{width:26px;height:5px;border:1px solid var(--orange);border-radius:50%;margin:0 3px}
.sidebar h3{font-weight:400;font-size:13px;padding:16px 0 6px;border-bottom:1px solid var(--rust-line)}
.cats{list-style:none;margin-top:6px;font-size:7.5px;line-height:20px}
.cats li::before{content:"• "}
.sidebar h4{font-weight:400;font-size:9.5px;margin-top:24px;text-transform:uppercase}
.email{margin-top:5px;height:16px;background:#fff;color:#222;font-size:7px;line-height:16px;padding-left:8px}
.subscribe{display:inline-block;margin-top:5px;background:var(--orange);color:var(--ink);font-size:7.5px;line-height:16px;padding:0 10px}
.dash{left:538px;top:1044px;width:208px;border-top:1px dashed #e9c7b0}

/* brands */
.brands{left:112px;top:1076px;width:590px;height:38px;display:flex;align-items:center;justify-content:space-between;font-size:13px;font-weight:700;color:#2a2a2a}

/* footer */
.footer{left:0;top:1117px;width:822px;height:83px;background:var(--footer)}
.foot-nav{left:82px;top:1158px;display:flex;font-size:7.5px;color:#fff;text-transform:uppercase}
.foot-nav span{padding:0 15px;border-left:1px solid #4a3226;line-height:16px}
.foot-nav span:first-child{border:0;padding-left:16px}
.copy{left:483px;top:1161px;font-size:6px;color:#fff;text-transform:uppercase}
.badge{left:660px;top:1141px;width:48px;height:46px;background:#fff;clip-path:polygon(0 0,100% 0,100% 80%,50% 100%,0 80%);display:flex;align-items:center;justify-content:center}
.badge span{width:26px;height:18px;border-radius:50%;background:#b7855a}
</style>
</head>
<body>

<header class="abs topbar">
  <div class="abs welcome">Welcome, <b>Guest!</b></div>
  <nav class="abs links"><span>CONTACT US</span><span>MY ACCOUNT</span><span>LOGIN</span></nav>
  <div class="abs cart">
    <svg width="12" height="11" viewBox="0 0 12 11"><path d="M0 1h2l2 6h6l1.5-4.5H3" fill="none" stroke="#fff" stroke-width="1.2"/><circle cx="5" cy="9.5" r="1" fill="#fff"/><circle cx="9" cy="9.5" r="1" fill="#fff"/></svg>
    <span>0 Items</span>
  </div>
  <div class="abs total">$0.00</div>
</header>
<a class="abs social one" aria-label="Chirpline"><span></span></a>
<a class="abs social two" aria-label="Profilo"><span></span></a>

<section class="abs hero" role="img" aria-label="Palomino horse trotting through a golden field at sunset"></section>
<div class="abs hero-copy">
  <div class="kicker">Horse Equipment Specialists</div>
  <h1>Great Deals &amp;<br>Special Offers</h1>
</div>
<div class="abs hero-btn">Shop now!</div>

<div class="abs navband"></div>
<nav class="abs nav">
  <a class="current">Who we are</a><a>How to buy</a><a>Special offers</a><a>Payments</a><a>Blog</a>
</nav>
<div class="abs logo"><span class="mark"></span>Brenvatoro</div>
<div class="abs dots"><i></i><i></i><i></i><i></i></div>

<main class="abs panel"></main>

<div class="abs tile english"><div class="photo" role="img" aria-label="English saddle against a red sunset"><small>English ride</small><b>Products</b></div></div>
<div class="abs tile western"><div class="photo" role="img" aria-label="Western rider standing with her horse under a blue sky"><small>Western ride</small><b>Products</b></div></div>
<div class="abs tile care"><div class="photo" role="img" aria-label="Two horses grazing in a golden pasture"><small>Accessories &amp;</small><b>Horse care</b></div></div>

<div class="abs promo gift">
  <div class="t1">Our gift to you</div>
  <div class="t2">A card with -50% discount</div>
  <hr>
  <div class="t3">Become a member</div>
</div>
<div class="abs promo stables" role="img" aria-label="Wooden stable interior">
  <div class="t1">Stables special</div>
  <div class="t2">Products to enrich your horse's home</div>
  <span class="small-btn">SHOP NOW!</span>
</div>
<div class="abs promo ship" role="img" aria-label="White horse galloping">
  <div class="t1">Spedizioni gratuite</div>
  <div class="t2">— on all your orders —</div>
</div>
<div class="abs promo best" role="img" aria-label="Leather saddle close-up">
  <div class="t1">I più venduti</div>
  <div class="t2">Up to -30% in discounts!</div>
  <span class="small-btn">SHOP NOW!</span>
</div>

<section class="abs news">
  <h2>Our latest news</h2>
  <div class="item"><div class="date">FEBRUARY 03 2014</div><b>Vivamus elementum semper nisi. Aenean vulputate eleifend tellus.</b> Aenean leo ligula, porttitor <a>dapibus in, viverra quis, feugiat a, tellus.</a></div>
  <div class="item"><div class="date">FEBRUARY 03 2014</div><b>Vivamus elementum semper nisi. Aenean vulputate eleifend tellus.</b> Aenean leo ligula, porttitor eu, consequat vitae, eleifend ac, enim. Aliquam lorem ante, <a>dapibus in, viverra quis, feugiat a, tellus.</a></div>
  <div class="item"><div class="date">FEBRUARY 03 2014</div><b>Vivamus elementum semper nisi. Aenean vulputate eleifend tellus.</b> Aenean leo ligula, porttitor eu, consequat vitae, <a>dapibus in, viverra quis, feugiat a, tellus.</a></div>
  <a class="more">More news</a>
</section>
<div class="abs promo saddle" role="img" aria-label="Tooled western saddle">
  <div class="t1">Build your own</div>
  <div class="t2">Saddle</div>
  <span class="small-btn">GET STARTED!</span>
</div>

<aside class="abs sidebar">
  <div class="search"><div class="field">Find a product</div><div class="go">SEARCH</div></div>
  <div class="divider"><i></i></div>
  <h3>CATEGORIES</h3>
  <ul class="cats">
    <li>RISERVATO AI MANEGGI</li><li>ABBIGLIAMENTO</li><li>SELLE E ACCESSORI</li><li>SOTTOPANCIA</li>
    <li>SOTTOSELLA E ACCESSORI</li><li>EQUIPAGGIAMENTO DEL CAVALLO</li><li>MORSI E FILETTI</li>
    <li>PROTEZIONI PER CAVALLO</li><li>COPERTE</li><li>CURA DEL CAVALLO</li><li>CURA DEL CUOIO</li>
    <li>ARTICOLI PER SCUDERIA</li><li>MASCALCIA</li><li>RECINZIONI ELETTRICHE</li><li>CARROZZE E FINIMENTI</li>
    <li>ARTICOLI REGALO E VARIE</li><li>TRAILER</li><li>MERCATINO USATO</li><li>HORSE EXTENSION</li><li>OFFERTE SPECIALI</li>
  </ul>
  <div class="divider"><i></i></div>
  <h4>Join our newsletter!</h4>
  <div class="email">Enter your email address</div>
  <span class="subscribe">SUBSCRIBE</span>
</aside>
<div class="abs dash"></div>

<div class="abs brands">
  <span>Marvetti</span><span>Tollbrook</span><span>Fernhollow</span><span>Velassi</span><span>Orvenza</span><span>Dunmere Ranch</span>
</div>

<footer class="abs footer"></footer>
<nav class="abs foot-nav"><span>Who we are</span><span>How to buy</span><span>Special offers</span><span>Payments</span><span>Blog</span></nav>
<div class="abs copy">Copyright 2014 Brenvatoro - Privacy policy</div>
<div class="abs badge"><span></span></div>

</body>
</html>
```